Brava Nest (Smart Home, Installation, Repair Industry) (Contest)

Looking for a website design for my company
Services we offer:
Phone Repair
TV Mounting
Security Camera Installation
Networking / Wi-Fi
Smart Home Services
IT Support

Looking for a website similar to trovely.example

Few tabs
About Us
Contact Us
Areas Served
Pricing and Services

```html
<!DOCTYPE html>
<html lang="en">
<head>
<meta charset="utf-8">
<title>Brava Nest — Smart Home, Installation, Repair</title>
<link href="https://fonts.googleapis.com/css2?family=Raleway:wght@500;600;700;800&family=Open+Sans:wght@400;600;700&display=swap" rel="stylesheet">
<style>
:root{
  --orange:#f7931e;
  --ink:#333333;
  --text:#555555;
  --muted:#8a8a8a;
  --band:#eeeff1;
  --line:#cfcfcf;
  --white:#ffffff;
  --hero-a:#e9e2d8;
  --hero-b:#cbbfae;
}
*{box-sizing:border-box;margin:0;padding:0}
html,body{width:1200px;height:4278px;overflow:hidden;background:var(--white)}
body{position:relative;font-family:"Open Sans",Arial,sans-serif;color:var(--text)}
.abs{position:absolute}
h1,h2,h3,h4,.brand,.nav a{font-family:"Raleway",Arial,sans-serif}

/* header / hero */
.hero-photo{left:0;top:0;width:1200px;height:626px}
.brand{left:112px;top:36px;font-size:56px;font-weight:800;color:var(--orange);letter-spacing:-1px}
.nav{top:58px;left:530px;display:flex;gap:0}
.nav a{position:absolute;white-space:nowrap;font-size:17px;font-weight:600;color:var(--ink);text-decoration:none}
.hero-title{left:110px;top:158px;font-size:48px;line-height:58px;font-weight:700;color:var(--ink)}
.hero-text{left:112px;top:348px;font-size:17px;line-height:29px;color:var(--text)}
.btn{display:flex;align-items:center;justify-content:center;border-radius:30px;font-family:"Open Sans",Arial,sans-serif;font-weight:700;font-size:18px;letter-spacing:.3px}
.btn-orange{left:112px;top:436px;width:206px;height:60px;background:var(--orange);color:var(--white)}

/* section heads */
.sec-head{left:0;width:1200px;text-align:center;font-size:38px;font-weight:600;color:var(--ink)}
.sec-head span{color:var(--orange)}
.divider{left:500px;width:200px;height:16px}
.divider::before{content:"";position:absolute;left:0;right:0;top:8px;border-top:1px solid var(--line)}
.divider::after{content:"";position:absolute;left:93px;top:1px;width:14px;height:14px;border-radius:50%;background:var(--orange);box-shadow:0 0 0 3px var(--white)}
.divider.on-band::after{box-shadow:0 0 0 3px var(--band)}
.divider.on-orange::before{border-color:rgba(255,255,255,.7)}
.divider.on-orange::after{background:var(--white);box-shadow:0 0 0 3px var(--orange)}
.lead{left:220px;width:760px;text-align:center;font-size:14px;line-height:28px;color:var(--text)}

/* features */
.feature-ring{width:96px;height:96px;border-radius:50%;border:1.5px solid #9a9a9a;display:flex;align-items:center;justify-content:center;background:var(--white)}
.feature-text{font-size:19px;line-height:28px;color:var(--text)}

/* house */
.house{left:112px;top:1010px;width:836px;height:346px;background:linear-gradient(180deg,#e8ecef 0%,#b9c1c6 55%,#5c6a5a 100%)}
.spot{width:100px;height:100px;border-radius:50%;border:9px solid rgba(247,147,30,.55);background:rgba(255,255,255,.9);display:flex;align-items:center;justify-content:center;text-align:center;font-family:"Open Sans",Arial,sans-serif;font-size:13px;line-height:19px;font-weight:600;color:var(--ink)}

/* services */
.svc{width:200px;text-align:center}
.svc svg{display:block;margin:0 auto}
.svc p{margin-top:18px;font-size:20px;line-height:26px;color:var(--ink);font-family:"Raleway",Arial,sans-serif;font-weight:500}

/* technicians */
.tech-card{top:2120px;width:308px;height:302px;border:2px solid #bdbdbd;border-radius:3px;background:var(--white);text-align:center;padding-top:74px}
.tech-card h4{font-size:21px;font-weight:700;color:var(--ink);line-height:28px}
.tech-card .role{font-size:17px;line-height:28px;color:var(--text)}
.stars{color:var(--orange);font-size:17px;letter-spacing:2px;margin:6px 0 14px}
.tech-card .bio{font-size:14px;line-height:27px;color:var(--muted);padding:0 18px}
.avatar{top:2056px;width:124px;height:124px;border-radius:50%;background:#bdbdbd;overflow:hidden}
.avatar::before{content:"";position:absolute;left:40px;top:24px;width:44px;height:44px;border-radius:50%;background:var(--white)}
.avatar::after{content:"";position:absolute;left:22px;top:76px;width:80px;height:70px;border-radius:40px 40px 0 0;background:var(--white)}
.arrow{top:2254px}

/* blog */
.post-img{top:2674px;width:304px;height:203px}
.post-title{top:2912px;width:304px;font-size:18px;line-height:29px;font-weight:700;color:var(--ink);font-family:"Raleway",Arial,sans-serif}
.post-meta{top:2980px;font-size:14px;color:var(--muted);display:flex;align-items:center;gap:6px}
.post-meta .dot{color:var(--orange)}
.post-excerpt{top:3017px;width:304px;font-size:14px;line-height:27px;color:var(--muted)}

/* partners */
.partner{top:3294px;width:183px;height:98px;border:2px solid #d3d3d3;display:flex;align-items:center;justify-content:center;font-family:"Raleway",Arial,sans-serif;font-weight:700;font-size:30px;color:#a8a8a8}

/* call to action */
.cta-title{left:0;width:1200px;text-align:center;top:3540px;font-size:38px;font-weight:600;color:var(--white)}
.cta-text{left:230px;width:740px;top:3632px;text-align:center;font-size:16px;line-height:31px;color:var(--white)}
.btn-white{left:498px;top:3728px;width:205px;height:62px;background:var(--white);color:var(--ink)}

/* footer */
.foot-head{top:3920px;font-size:20px;font-weight:700;color:var(--ink);font-family:"Raleway",Arial,sans-serif}
.foot-list{top:3966px;list-style:none;font-size:14px;line-height:26px;color:var(--text)}
.news-text{left:727px;top:3966px;width:310px;font-size:14px;line-height:26px;color:var(--text)}
.news-input{left:727px;top:4040px;width:269px;height:44px;border:1px solid #cfcfcf;border-right:none;display:flex;align-items:center;padding-left:20px;gap:8px;font-size:14px;color:var(--muted)}
.news-btn{left:996px;top:4040px;width:92px;height:44px;background:var(--orange);color:var(--white);font-size:13px;font-weight:700;display:flex;align-items:center;justify-content:center}
.social{top:4112px;width:46px;height:46px;border:1.5px solid var(--orange);border-radius:50%;display:flex;align-items:center;justify-content:center}
.social::after{content:"";width:10px;height:10px;border-radius:50%;background:var(--orange)}
.foot-rule{left:98px;top:4200px;width:1004px;border-top:1px solid #d6d6d6}
.copyright{left:0;width:1200px;top:4222px;text-align:center;font-size:14px;color:var(--text)}
</style>
</head>
<body>

<!-- Hero -->
<svg class="abs hero-photo" viewBox="0 0 1200 626" role="img" aria-label="Photo of a woman relaxing on a white sofa using her phone in a bright living room">
  <defs>
    <linearGradient id="heroGrad" x1="0" y1="0" x2="1" y2="1">
      <stop offset="0" stop-color="#f4f0ea"/>
      <stop offset=".55" stop-color="#e6dfd4"/>
      <stop offset="1" stop-color="#b99a78"/>
    </linearGradient>
  </defs>
  <polygon points="0,0 1200,0 1200,626 0,540" fill="url(#heroGrad)"/>
</svg>

<div class="abs brand">Brava Nest</div>
<nav class="abs nav" style="left:0;top:58px">
  <a style="left:530px">About Us</a>
  <a style="left:644px">Contact Us</a>
  <a style="left:773px">Areas Served</a>
  <a style="left:922px">Pricing</a>
  <a style="left:1016px">Services</a>
</nav>

<h1 class="abs hero-title">Smart Home,<br>Installation,<br>Repair Industry</h1>
<p class="abs hero-text">Nemo enim ipsam voluptatem quiaolu<br>ptas sit aspernatur aut odi</p>
<div class="abs btn btn-orange">BOOK A SERVICE</div>

<!-- Welcome -->
<h2 class="abs sec-head" style="top:652px">Welcome to <span>Brava Nest</span></h2>
<div class="abs divider" style="top:714px"></div>
<p class="abs lead" style="top:749px">Sed ut perspiciatis unde omnis iste natus error sit voluptatem accusantium doloremque laudantium, totam rem aperiam, eaque ipsa quae ab illo inventore veritatis et quasi architecto beatae vitae</p>

<div class="abs feature-ring" style="left:110px;top:838px">
  <svg width="44" height="44" viewBox="0 0 44 44"><path d="M8 22a14 14 0 1 0 4-10" fill="none" stroke="#f7931e" stroke-width="4" stroke-linecap="round"/><path d="M6 6v9h9" fill="none" stroke="#f7931e" stroke-width="4" stroke-linecap="round" stroke-linejoin="round"/></svg>
</div>
<p class="abs feature-text" style="left:225px;top:857px">24/7 support service<br>Guaranteed</p>

<div class="abs feature-ring" style="left:475px;top:838px">
  <svg width="44" height="44" viewBox="0 0 44 44"><rect x="6" y="20" width="8" height="18" rx="1" fill="#f7931e"/><path d="M17 20l8-14c3 0 4 2 3 6l-1 6h9c2 0 3 2 3 4l-3 13c-1 2-2 3-4 3H17z" fill="#f7931e"/></svg>
</div>
<p class="abs feature-text" style="left:590px;top:857px">Trusted<br>Technicians</p>

<div class="abs feature-ring" style="left:787px;top:838px">
  <svg width="44" height="44" viewBox="0 0 44 44"><path d="M30 6a9 9 0 0 0-8 12L7 33a3 3 0 0 0 4 4l15-15a9 9 0 0 0 12-8l-6 3-4-4 3-6z" fill="#f7931e"/></svg>
</div>
<p class="abs feature-text" style="left:903px;top:857px">Hundreds of repair<br>and installation</p>

<!-- House illustration -->
<div class="abs house" role="img" aria-label="Illustration of a modern two-storey house at dusk with service hotspots"></div>
<div class="abs spot" style="left:775px;top:993px">HVAC<br>Repair</div>
<div class="abs spot" style="left:411px;top:1073px">Home<br>Appliances</div>
<div class="abs spot" style="left:620px;top:1061px">Smart<br>Home<br>Installation</div>
<div class="abs spot" style="left:224px;top:1167px">Home<br>Appliances</div>
<div class="abs spot" style="left:374px;top:1201px">TV<br>Mounting</div>
<div class="abs spot" style="left:663px;top:1233px">Garage<br>Door<br>Repair</div>
<div class="abs spot" style="left:451px;top:1287px">Plumbing<br>Services</div>

<!-- Services band -->
<svg class="abs" style="left:0;top:1400px" width="1200" height="502" viewBox="0 0 1200 502"><polygon points="0,70 1200,5 1200,502 0,437" fill="#eeeff1"/></svg>
<h2 class="abs sec-head" style="top:1484px">Services <span>We Offer</span></h2>
<div class="abs divider on-band" style="top:1544px"></div>

<div class="abs svc" style="left:79px;top:1612px">
  <svg width="110" height="110" viewBox="0 0 110 110"><rect x="42" y="6" width="46" height="98" rx="7" fill="none" stroke="#555" stroke-width="2.5"/><line x1="58" y1="14" x2="72" y2="14" stroke="#555" stroke-width="2.5"/><rect x="4" y="48" width="52" height="12" rx="3" fill="none" stroke="#f7931e" stroke-width="2.5"/><circle cx="84" cy="54" r="12" fill="none" stroke="#f7931e" stroke-width="2.5"/><circle cx="84" cy="54" r="4" fill="#f7931e"/></svg>
  <p>Phone<br>Repair</p>
</div>
<div class="abs svc" style="left:253px;top:1612px">
  <svg width="110" height="110" viewBox="0 0 110 110"><path d="M20 30a38 38 0 0 0 50 50z" fill="none" stroke="#555" stroke-width="2.5"/><line x1="45" y1="55" x2="68" y2="32" stroke="#555" stroke-width="2.5"/><path d="M38 72l-8 26h40l-8-26" fill="none" stroke="#555" stroke-width="2.5"/><path d="M76 20a16 16 0 0 1 14 14M78 10a26 26 0 0 1 22 22" fill="none" stroke="#f7931e" stroke-width="2.5"/></svg>
  <p>TV<br>Mounting</p>
</div>
<div class="abs svc" style="left:427px;top:1612px">
  <svg width="110" height="110" viewBox="0 0 110 110"><rect x="14" y="22" width="70" height="18" rx="3" fill="none" stroke="#555" stroke-width="2.5"/><path d="M20 40v18a30 30 0 0 0 58 0V40" fill="none" stroke="#555" stroke-width="2.5"/><circle cx="50" cy="66" r="8" fill="none" stroke="#f7931e" stroke-width="2.5"/><path d="M78 14a12 12 0 0 1 12 12M80 4a22 22 0 0 1 20 20" fill="none" stroke="#f7931e" stroke-width="2.5"/></svg>
  <p>Security Camera<br>Installation</p>
</div>
<div class="abs svc" style="left:600px;top:1612px">
  <svg width="110" height="110" viewBox="0 0 110 110"><circle cx="52" cy="58" r="42" fill="none" stroke="#555" stroke-width="2.5"/><ellipse cx="52" cy="58" rx="18" ry="42" fill="none" stroke="#555" stroke-width="2.5"/><line x1="10" y1="58" x2="94" y2="58" stroke="#555" stroke-width="2.5"/><path d="M80 14a10 10 0 0 1 10 10M82 4a20 20 0 0 1 18 18" fill="none" stroke="#f7931e" stroke-width="2.5"/></svg>
  <p>Networking<br>/ Wi-Fi</p>
</div>
<div class="abs svc" style="left:775px;top:1612px">
  <svg width="110" height="110" viewBox="0 0 110 110"><path d="M14 50L55 12l41 38v48H14z" fill="none" stroke="#555" stroke-width="2.5" stroke-linejoin="round"/><path d="M40 60a20 20 0 0 1 30 0M46 68a11 11 0 0 1 18 0" fill="none" stroke="#f7931e" stroke-width="2.5"/><circle cx="55" cy="76" r="3" fill="#f7931e"/></svg>
  <p>Smart Home<br>Services</p>
</div>
<div class="abs svc" style="left:948px;top:1612px">
  <svg width="110" height="110" viewBox="0 0 110 110"><circle cx="55" cy="55" r="42" fill="none" stroke="#555" stroke-width="2.5"/><circle cx="55" cy="55" r="26" fill="none" stroke="#f7931e" stroke-width="2.5" stroke-dasharray="10 5"/><circle cx="55" cy="55" r="12" fill="none" stroke="#f7931e" stroke-width="2.5"/></svg>
  <p>IT<br>Support</p>
</div>

<!-- Technicians -->
<h2 class="abs sec-head" style="top:1940px">Our Top <span>Technicians</span></h2>
<div class="abs divider" style="top:1998px"></div>

<svg class="abs arrow" style="left:42px" width="22" height="34" viewBox="0 0 22 34"><path d="M18 3L4 17l14 14" fill="none" stroke="#666" stroke-width="3"/></svg>
<svg class="abs arrow" style="left:1134px" width="22" height="34" viewBox="0 0 22 34"><path d="M4 3l14 14L4 31" fill="none" stroke="#666" stroke-width="3"/></svg>

<div class="abs tech-card" style="left:110px">
  <h4>John</h4><p class="role">Brava Nest Technician<br>Los Angeles, CA</p>
  <div class="stars">★★★★★</div>
  <p class="bio">Neque porro quisquam est, qui do lorem ipsum quia dolor sit amet, conse ctetur, adipisci velit, sed qu</p>
</div>
<div class="abs avatar" style="left:202px" role="img" aria-label="Technician profile placeholder"></div>

<div class="abs tech-card" style="left:446px">
  <h4>Clara</h4><p class="role">Brava Nest Technician<br>Los Angeles, CA</p>
  <div class="stars">★★★★★</div>
  <p class="bio">Neque porro quisquam est, qui do lorem ipsum quia dolor sit amet, conse ctetur, adipisci velit, sed qu</p>
</div>
<div class="abs avatar" style="left:538px" role="img" aria-label="Technician profile placeholder"></div>

<div class="abs tech-card" style="left:780px">
  <h4>Henry</h4><p class="role">Brava Nest Technician<br>Los Angeles, CA</p>
  <div class="stars">★★★★★</div>
  <p class="bio">Neque porro quisquam est, qui do lorem ipsum quia dolor sit amet, conse ctetur, adipisci velit, sed qu</p>
</div>
<div class="abs avatar" style="left:872px" role="img" aria-label="Technician profile placeholder"></div>

<!-- Blog band -->
<svg class="abs" style="left:0;top:2472px" width="1200" height="640" viewBox="0 0 1200 640"><polygon points="0,70 1200,0 1200,640 0,640" fill="#eeeff1"/></svg>
<h2 class="abs sec-head" style="top:2558px">Brava Nest <span>Blog</span></h2>
<div class="abs divider on-band" style="top:2616px"></div>

<div class="abs post-img" style="left:112px;background:linear-gradient(135deg,#e9e6e1,#c9a58a)" role="img" aria-label="Photo of a woman adjusting a wall-mounted smart home panel"></div>
<h3 class="abs post-title" style="left:112px">Nam libero tempore, cum soluta nobis est eligendi</h3>
<div class="abs post-meta" style="left:112px"><span class="dot">▣</span>May 23, 2020 &nbsp;| <span class="dot">●</span>John</div>
<p class="abs post-excerpt" style="left:112px">At vero eos et accusamus et iusto odio digni ssi mos ducimus qui blanditi..</p>

<div class="abs post-img" style="left:449px;background:linear-gradient(135deg,#d8d2cb,#6f8f8a)" role="img" aria-label="Photo of a man installing a smart door lock"></div>
<h3 class="abs post-title" style="left:449px">Nam libero tempore, cum soluta nobis est eligendi</h3>
<div class="abs post-meta" style="left:449px"><span class="dot">▣</span>May 23, 2020 &nbsp;| <span class="dot">●</span>John</div>
<p class="abs post-excerpt" style="left:449px">At vero eos et accusamus et iusto odio digni ssi mos ducimus qui blanditi..</p>

<div class="abs post-img" style="left:786px;background:linear-gradient(135deg,#f0f2f4,#4a6a8e)" role="img" aria-label="Photo of hands holding a tablet showing a home control app"></div>
<h3 class="abs post-title" style="left:786px">Nam libero tempore, cum soluta nobis est eligendi</h3>
<div class="abs post-meta" style="left:786px"><span class="dot">▣</span>May 23, 2020 &nbsp;| <span class="dot">●</span>John</div>
<p class="abs post-excerpt" style="left:786px">At vero eos et accusamus et iusto odio digni ssi mos ducimus qui blanditi..</p>

<!-- Trusted by -->
<h2 class="abs sec-head" style="top:3182px">Trusted <span>By</span></h2>
<div class="abs divider" style="top:3238px"></div>
<div class="abs partner" style="left:112px">Northlane</div>
<div class="abs partner" style="left:310px">Keelwork</div>
<div class="abs partner" style="left:508px">Orbitra</div>
<div class="abs partner" style="left:707px">Solvane</div>
<div class="abs partner" style="left:905px">Pinemark</div>

<!-- Call to action -->
<svg class="abs" style="left:0;top:3436px" width="1200" height="432" viewBox="0 0 1200 432"><polygon points="0,66 1200,0 1200,362 0,430" fill="#f7931e"/></svg>
<h2 class="abs cta-title">Ready To Get Started?</h2>
<div class="abs divider on-orange" style="top:3596px"></div>
<p class="abs cta-text">Sed ut perspiciatis unde omnis iste natus error sit voluptatem accusantium doloremque lauda ntium, totam rem aperiam, eaque ipsa quae ab illo inventore veritatis et quasi archi</p>
<div class="abs btn btn-white">BOOK A SERVICE</div>

<!-- Footer -->
<h4 class="abs foot-head" style="left:110px">Company</h4>
<ul class="abs foot-list" style="left:111px">
  <li>About Us</li><li>How It Works</li><li>Become a Tech</li><li>Pricing</li><li>Careers</li><li>Blog</li><li>Newsroom</li><li>Media inquiries</li>
</ul>
<h4 class="abs foot-head" style="left:282px">Resources</h4>
<ul class="abs foot-list" style="left:283px">
  <li>Phone Repair</li><li>TV Mounting</li><li>Security Camera Installation</li><li>Networking / Wi-Fi</li><li>Smart Home Services</li><li>IT Support</li>
</ul>
<h4 class="abs foot-head" style="left:514px">Legal</h4>
<ul class="abs foot-list" style="left:515px;line-height:28px">
  <li>Help</li><li>FAQ</li><li>Terms &amp; conditions</li><li>Return Policy</li><li>Customer Support</li><li>Contact Us</li>
</ul>
<h4 class="abs foot-head" style="left:726px">Newsletter Subscription</h4>
<p class="abs news-text">Register your Email Address to get informa- tion about us</p>
<div class="abs news-input"><svg width="14" height="11" viewBox="0 0 14 11"><rect x=".5" y=".5" width="13" height="10" fill="none" stroke="#8a8a8a"/><path d="M.5 .5l6.5 5 6.5-5" fill="none" stroke="#8a8a8a"/></svg>Email Address</div>
<div class="abs news-btn">SUBSCRIBE</div>
<div class="abs social" style="left:727px" aria-label="Social link"></div>
<div class="abs social" style="left:781px" aria-label="Social link"></div>
<div class="abs social" style="left:835px" aria-label="Social link"></div>

<div class="abs foot-rule"></div>
<p class="abs copyright">Copyrights © 2020, Brava Nest.</p>

</body>
</html>
```